New letterhead design for legal, public interest law firm

THIS IS FOR A LETTERHEAD DESIGN CONTEST , PLEASE REFRAIN FROM SUBMITTING JUST LOGO PROPOSALS AND BUSINESS CARD. LOGO AND BUSINESS CARD PROJECTS WILL BE AWARDED TO THE WINNER OF THE LETTERHEAD DESIGN.
Looking for a timeless, elegant and modern design for our letterhead and logo. Our website is www.hlrbvwn.org so you can incorporate the mission, vision and values into the design. As we also included a request for a NEW LOGO design, please be sure to include logo design options.
We are a public interest criminal defense organization that represents indigent people charged with federal crimes. Please weave the mission/vision/values and our practice area into the logo design.
Target Market(s)
Judges, clients, attorneys, family members of our clients.
Industry/Entity Type
Legal
Contact Information for Business Card
Include line for address, direct line, fax, email address, website address. Remember to incorporate NEW LOGO design.
Logo Text
Harbor Legal Advocates Northern Bureau of Westmoor
Requirements
Must have
- Please remember this project is also to design us a NEW LOGO. Please do not incorporate the existing logo into the new letterhead design.
Nice to have
- Nice to see some logo samples incorporating symbolism for justice, California specific imagery.
Should not have
- New logo should NOT have any traditional/typical legal related images (e.g., scales of justice, etc.)

```html
<!DOCTYPE html>
<html lang="en">
<head>
<meta charset="utf-8">
<title>Harbor Legal Advocates – Stationery</title>
<link href="https://fonts.googleapis.com/css2?family=Open+Sans:wght@400;600&family=Roboto+Condensed:wght@400;700&display=swap" rel="stylesheet">
<style>
  :root {
    --brand-blue: #1155a6;
    --brand-orange: #f28c1e;
    --ink: #4a4a4a;
    --paper: #ffffff;
    --desk: #eeeff2;
    --signature-tone: #e6e6e8;
  }
  * { margin: 0; padding: 0; box-sizing: border-box; }
  html, body { width: 1200px; height: 800px; overflow: hidden; }
  body { background: var(--desk); position: relative; font-family: "Open Sans", sans-serif; color: var(--ink); }
  .icon { width: 1em; height: 1em; fill: var(--brand-blue); vertical-align: -0.12em; margin-right: 0.3em; }

  /* Letterhead */
  .letterhead { position: absolute; left: 364px; top: 67px; width: 472px; height: 666px; background: var(--paper); }
  .wordmark { font-family: "Open Sans", sans-serif; font-weight: 600; color: var(--brand-blue); text-transform: uppercase; letter-spacing: 0.06em; line-height: 1.35; }
  .letterhead .wordmark { position: absolute; left: 41px; top: 72px; font-size: 9.5px; display: flex; align-items: center; gap: 7px; }
  .wordmark .mark-dot { width: 9px; height: 9px; border-radius: 50%; background: var(--brand-blue); flex: none; }
  .letterhead .contact { position: absolute; left: 344px; top: 65px; list-style: none; font-size: 9.2px; line-height: 12.7px; color: #3d3d3d; }
  .letter-body { position: absolute; left: 42px; top: 160px; width: 390px; font-size: 8.5px; line-height: 12.9px; }
  .letter-body p { text-align: justify; margin-bottom: 12.9px; }
  .letter-body p.last-paragraph { text-align: left; }
  .letter-body .closing { margin-bottom: 8px; }
  .signature-area { width: 56px; height: 54px; background: var(--signature-tone); }
  .letter-footer { position: absolute; left: 0; top: 635px; width: 472px; height: 18px; display: flex; gap: 3px; }
  .band-blue { flex: 1; background: var(--brand-blue); color: #fff; font-size: 9px; display: flex; align-items: center; justify-content: center; }
  .band-orange { width: 56px; background: var(--brand-orange); }

  /* Business card front */
  .card { position: absolute; left: 107px; width: 192px; height: 124px; }
  .card-front { top: 374px; background: var(--paper); }
  .card-front .wordmark { position: absolute; left: 18px; top: 47px; width: 76px; font-size: 5.4px; letter-spacing: 0.03em; }
  .card-divider { position: absolute; left: 96px; top: 36px; width: 1px; height: 52px; background: var(--brand-orange); }
  .card-details { position: absolute; left: 104px; top: 36px; font-family: "Roboto Condensed", sans-serif; }
  .card-name { font-weight: 700; color: var(--brand-blue); font-size: 7.2px; line-height: 8px; }
  .card-role { color: var(--brand-orange); font-size: 5.8px; line-height: 7px; margin-bottom: 4px; }
  .card-details ul { list-style: none; font-size: 5.6px; line-height: 9.3px; color: #3d3d3d; }
  .card-footer { position: absolute; left: 0; top: 104px; width: 192px; height: 12px; display: flex; gap: 2px; }
  .card-footer .band-blue { font-family: "Roboto Condensed", sans-serif; font-size: 5.8px; }
  .card-footer .band-orange { width: 22px; }

  /* Business card back */
  .card-back { top: 546px; background: var(--brand-blue); display: flex; align-items: center; justify-content: center; }
  .card-back .wordmark { color: #fff; font-size: 8.5px; text-align: center; letter-spacing: 0.05em; }
</style>
</head>
<body>
<svg width="0" height="0" style="position:absolute">
  <defs>
    <symbol id="i-phone" viewBox="0 0 16 16"><path d="M3.6 1.2 6 3.6 4.8 5.6c.9 2 2.6 3.7 4.6 4.6l2-1.2 2.4 2.4-1.4 2.4C6.8 13.6 2.4 9.2 1.2 2.6z"/></symbol>
    <symbol id="i-fax" viewBox="0 0 16 16"><path d="M4 1h8v4H4zM1 6h14v6h-3v3H4v-3H1zm4 4v4h6v-4z"/></symbol>
    <symbol id="i-mail" viewBox="0 0 16 16"><path d="M1 3h14v10H1zm1.5 1.5v.3L8 9l5.5-4.2v-.3zm0 2.2v4.8h11V6.7L8 10.9z"/></symbol>
    <symbol id="i-web" viewBox="0 0 16 16"><path d="M8 1a7 7 0 1 0 0 14A7 7 0 0 0 8 1zm0 1.5a5.5 5.5 0 0 1 5.5 5.5H2.5A5.5 5.5 0 0 1 8 2.5zM2.6 9h10.8A5.5 5.5 0 0 1 2.6 9z"/></symbol>
  </defs>
</svg>

<main class="letterhead">
  <div class="wordmark"><span class="mark-dot"></span><span>Harbor Legal Advocates<br>Northern Bureau of Westmoor</span></div>
  <ul class="contact">
    <li><svg class="icon"><use href="#i-phone"/></svg>+56910427391</li>
    <li><svg class="icon"><use href="#i-fax"/></svg>+56910427391</li>
    <li><svg class="icon"><use href="#i-mail"/></svg>info@hlrbvwn.org</li>
    <li><svg class="icon"><use href="#i-web"/></svg>www.hlrbvwn.org</li>
  </ul>
  <div class="letter-body">
    <p class="salutation">Dear customer,</p>
    <p>Lorem ipsum dolor sit amet, consectetur adipisicing elit, sed do eiusmod tempor incididunt ut labore et dolore magna aliqua. Ut enim ad minim veniam, quis nostrud exercitation ullamco laboris nisi ut aliquip ex ea commodo consequat. Duis aute irure dolor in reprehenderit in voluptate velit esse cillum dolore eu fugiat nulla pariatur. Excepteur sint occaecat cupidatat non proident, sunt in culpa qui officia deserunt mollit anim id est laborum.</p>
    <p>Lorem ipsum dolor sit amet, consectetur adipisicing elit, sed do eiusmod tempor incididunt ut labore et dolore magna aliqua. Ut enim ad minim veniam, quis nostrud exercitation ullamco laboris nisi ut aliquip ex ea commodo consequat. Duis aute irure dolor in reprehenderit in voluptate velit esse cillum dolore eu fugiat nulla pariatur. Excepteur sint occaecat cupidatat non proident, sunt in culpa qui officia deserunt mollit anim id est laborum.</p>
    <p>Lorem ipsum dolor sit amet, consectetur adipisicing elit, sed do eiusmod tempor incididunt ut labore et dolore magna aliqua. Ut enim ad minim veniam, quis nostrud exercitation ullamco laboris nisi ut aliquip ex ea commodo consequat. Duis aute irure dolor in reprehenderit in voluptate velit esse cillum dolore eu fugiat nulla pariatur. Excepteur sint occaecat cupidatat non proident, sunt in culpa qui officia deserunt mollit anim id est laborum.</p>
    <p class="last-paragraph">Lorem ipsum dolor sit amet, consectetur adipisicing elit, sed do eiusmod tempor incididunt ut labore et dolore magna aliqua. Ut enim ad minim veniam, quis nostrud exercitation ullamco laboris nisi ut aliquip ex ea commodo consequat. Duis aute irure dolor in reprehenderit.</p>
    <p class="closing">Yours Sincerely,</p>
    <div class="signature-area" role="img" aria-label="Handwritten signature"></div>
  </div>
  <footer class="letter-footer">
    <div class="band-blue">PO Box 4820 Kestrel Park NSW 2190 Bangline, UK</div>
    <div class="band-orange"></div>
  </footer>
</main>

<section class="card card-front">
  <div class="wordmark">Harbor Legal Advocates Northern Bureau of Westmoor</div>
  <div class="card-divider"></div>
  <div class="card-details">
    <div class="card-name">DANA WHITCOMBE</div>
    <div class="card-role">Managing Director</div>
    <ul>
      <li><svg class="icon"><use href="#i-phone"/></svg>+56910427391</li>
      <li><svg class="icon"><use href="#i-fax"/></svg>+56910427391</li>
      <li><svg class="icon"><use href="#i-mail"/></svg>info@hlrbvwn.org</li>
      <li><svg class="icon"><use href="#i-web"/></svg>www.hlrbvwn.org</li>
    </ul>
  </div>
  <div class="card-footer">
    <div class="band-blue">PO Box 4820 Kestrel Park NSW 2190 USA</div>
    <div class="band-orange"></div>
  </div>
</section>

<section class="card card-back">
  <div class="wordmark">Harbor Legal Advocates<br>Northern Bureau of Westmoor</div>
</section>
</body>
</html>
```